Design some Business Cards for Tavro

Thanks to everyone for their efforts. I will just be reviewing the first two entries from each contestant, so I'd suggest withdrawing entries which are not your favorites & going with your best two. Many thanks, Derek

I was after a double sided business card for tavro.com.au. Tavro is a billing app and website for tradesman and service providers who move from site to site.

Firstly design for Derek Holm with mobile 0481 555 907 & email demo@tavro.com.au.

Logo is attached, so please work with those colours. I've also included our url if you believe that is worth building in.

I would like the original working files and the business card will need to be produced for 3 different employees when the winner is selected.

Additional TAVRO text files if this helps.

```html
<!DOCTYPE html>
<html lang="en">
<head>
<meta charset="utf-8">
<title>Tavro Business Cards</title>
<link href="https://fonts.googleapis.com/css2?family=Open+Sans:wght@400;600;700&display=swap" rel="stylesheet">
<style>
  :root {
    --backdrop: #e9e6e1;
    --card: #ffffff;
    --ink: #151515;
    --brand-red: #d8232a;
    --muted: #3a3a3a;
    --rule: #c9c9c9;
    --band-dark: #1b1b1b;
  }
  * { box-sizing: border-box; margin: 0; padding: 0; }
  html, body {
    width: 1200px; height: 912px; overflow: hidden;
    background: var(--backdrop);
    font-family: "Open Sans", Arial, sans-serif;
  }
  .stage { position: relative; width: 1200px; height: 912px; }
  .card {
    position: absolute; width: 540px; height: 308px;
    background: var(--card);
    box-shadow: 0 10px 28px rgba(0,0,0,.18);
    overflow: hidden;
  }
  .card-front { left: 40px; top: 170px; }
  .card-back { left: 620px; top: 430px; }

  .brand { display: flex; align-items: center; gap: 14px; }
  .brand-dot {
    width: 58px; height: 58px; border-radius: 50%;
    background: var(--brand-red);
    flex: none;
  }
  .brand-name {
    font-weight: 700; color: var(--ink);
    letter-spacing: 4px; line-height: 1;
  }

  .card-front .brand { position: absolute; left: 96px; top: 104px; }
  .card-front .brand-dot { width: 74px; height: 74px; }
  .card-front .brand-name { font-size: 64px; }
  .front-url {
    position: absolute; left: 186px; top: 176px;
    font-size: 17px; font-weight: 700; letter-spacing: 1.5px;
    color: var(--brand-red);
  }

  .card-back .brand { position: absolute; left: 150px; top: 40px; }
  .card-back .brand-dot { width: 50px; height: 50px; }
  .card-back .brand-name { font-size: 46px; }
  .logo-rule {
    position: absolute; left: 214px; right: 0; top: 104px;
    height: 1px; background: var(--rule);
  }

  .holder { position: absolute; left: 34px; top: 150px; right: 0; }
  .holder-name {
    display: flex; align-items: center; gap: 10px;
    font-size: 19px; font-weight: 600; color: var(--brand-red);
  }
  .holder-name::after {
    content: ""; flex: 1; height: 1px; background: var(--rule); margin-top: 4px;
  }
  .holder-title { font-size: 11px; color: var(--muted); margin-top: 1px; }

  .contact-list { list-style: none; margin-top: 8px; }
  .contact-list li {
    display: flex; align-items: flex-start; gap: 9px;
    font-size: 11.5px; color: var(--muted); line-height: 1.3;
    margin-bottom: 4px;
  }
  .contact-icon { width: 14px; height: 14px; flex: none; margin-top: 1px; }

  .edge-band {
    position: absolute; left: 0; right: 0; bottom: 0; height: 22px;
    display: flex;
  }
  .edge-band-dark { flex: 7; background: var(--band-dark); }
  .edge-band-red { flex: 3; background: var(--brand-red); }
</style>
</head>
<body>
<main class="stage">

  <section class="card card-front" aria-label="Card front">
    <div class="brand">
      <span class="brand-dot"></span>
      <span class="brand-name">TAVRO</span>
    </div>
    <p class="front-url">WWW.TAVRO.COM.AU</p>
  </section>

  <section class="card card-back" aria-label="Card back">
    <div class="brand">
      <span class="brand-dot"></span>
      <span class="brand-name">TAVRO</span>
    </div>
    <div class="logo-rule"></div>

    <div class="holder">
      <p class="holder-name">Derek Holm</p>
      <p class="holder-title">Managing Director</p>
      <ul class="contact-list">
        <li>
          <svg class="contact-icon" viewBox="0 0 14 14" aria-hidden="true">
            <circle cx="7" cy="7" r="7" fill="var(--brand-red)"/>
            <path d="M4.6 3.8l1.3 1.4-.7.9c.4.9 1.1 1.6 2 2l.9-.7 1.4 1.3-.8 1.2c-2.4-.3-4.4-2.3-4.7-4.7z" fill="#fff"/>
          </svg>
          <span>0481 555 907</span>
        </li>
        <li>
          <svg class="contact-icon" viewBox="0 0 14 14" aria-hidden="true">
            <circle cx="7" cy="7" r="7" fill="var(--brand-red)"/>
            <rect x="3.6" y="4.6" width="6.8" height="4.8" fill="none" stroke="#fff" stroke-width="1"/>
            <path d="M3.6 4.8L7 7.3l3.4-2.5" fill="none" stroke="#fff" stroke-width="1"/>
          </svg>
          <span>demo@tavro.com.au</span>
        </li>
        <li>
          <svg class="contact-icon" viewBox="0 0 14 14" aria-hidden="true">
            <circle cx="7" cy="7" r="7" fill="var(--brand-red)"/>
            <circle cx="7" cy="7" r="3.4" fill="none" stroke="#fff" stroke-width="1"/>
            <path d="M3.6 7h6.8M7 3.6v6.8" stroke="#fff" stroke-width=".8"/>
          </svg>
          <span>www.tavro.com.au</span>
        </li>
        <li>
          <svg class="contact-icon" viewBox="0 0 14 14" aria-hidden="true">
            <circle cx="7" cy="7" r="7" fill="var(--brand-red)"/>
            <path d="M7 3.2a2.6 2.6 0 0 1 2.6 2.6C9.6 7.8 7 10.8 7 10.8S4.4 7.8 4.4 5.8A2.6 2.6 0 0 1 7 3.2z" fill="#fff"/>
            <circle cx="7" cy="5.8" r=".9" fill="var(--brand-red)"/>
          </svg>
          <span>Address goes here or city,<br>state and zip code</span>
        </li>
      </ul>
    </div>

    <div class="edge-band">
      <span class="edge-band-dark"></span>
      <span class="edge-band-red"></span>
    </div>
  </section>

</main>
</body>
</html>
```